Saveurs Du Matin

looking fo an e-commerce site something that will stand out the site domain will be saveursdumatin.example need somthing bold and refind as well; eye appealing and not too cartonish please visit our competetors to see waht we are going for they are (tastrovel.example, brenza4u.example and calvanopresses.example) this site should have multiple pages mainly looking for a layout to start the site and code.

PLEASE REMEMBER WE REQUIRE THE CODE....

Target Market(s)

anyone who loves food or is fasinated by it

Industry/Entity Type

E-Commerce

Requirements
Must have
• .an easy to work site that makes sense and that is not all over the place it should have in the navigation feature: Olive oils, Balsamic Vinegars, Misc. Vinegars and oils, Specialty salts, organic spices, Specialty Spices, Kitchen Tools. also pleas use our logo in the design i have attached below
Nice to have
• clean and some spices, salt, pepermills, morter and pistels, olive oils, trying to stick to a clean presentation
Should not have
• no cartoon figures or alike, anything too playfull

```html
<!DOCTYPE html>
<html lang="en">
<head>
<meta charset="utf-8">
<title>Saveurs Du Matin</title>
<link rel="stylesheet" href="https://fonts.googleapis.com/css2?family=Source+Sans+3:ital,wght@0,300;0,400;0,600;1,300;1,400&display=swap">
<style>
:root{
  --page:#f4f2ea;
  --band:#e9e6d6;
  --white:#ffffff;
  --brown:#8d4c22;
  --brown-mid:#a9622e;
  --tan:#b97a4a;
  --orange:#c9652f;
  --red:#a8252a;
  --cream:#e4e1c6;
  --cream-line:#d9d5b5;
  --text:#6a6a6a;
  --gold:#f2b22c;
  --dark:#3b3b3b;
}
*{box-sizing:border-box;margin:0;padding:0}
html,body{width:890px;height:1200px;overflow:hidden}
body{background:var(--page);font-family:"Source Sans 3",sans-serif;color:var(--text);position:relative}
.band{position:absolute;left:0;width:890px;top:176px;height:20px;background:var(--band);border-top:1px solid #dcd8c2;border-bottom:1px solid #dcd8c2}
.abs{position:absolute}
.toplinks{top:12px;right:74px;font-size:10px;color:#b2282b;display:flex;gap:12px;align-items:center}
.toplinks .sep{color:#b2282b}
.toplinks svg{vertical-align:-2px;margin-right:3px}
.sheet{left:66px;top:40px;width:758px;height:1082px;background:var(--white);box-shadow:0 0 6px rgba(0,0,0,.08)}
.brand{left:76px;top:62px;display:flex;align-items:center;gap:8px;color:var(--brown);font-size:17px;font-weight:400}
.brand .mark{width:22px;height:22px;border-radius:50%;background:var(--tan)}
.search{left:682px;top:58px;width:132px;height:23px;border:1px solid #d4d4d4;font-size:8.5px;color:#aaa;padding:5px 8px;display:flex;justify-content:space-between;align-items:center}
.nav{left:69px;top:170px;width:752px;height:37px;display:flex;background:linear-gradient(#ad6331,#8a4720);border-radius:4px 4px 0 0;overflow:hidden}
.nav a{color:#fff;font-size:11px;text-decoration:none;display:flex;align-items:center;justify-content:center;border-right:1px solid rgba(0,0,0,.18)}
.nav a:last-child{border-right:none}
.nav a.active{background:linear-gradient(#d3863c,#bf6e2c)}
.news{left:69px;top:214px;width:206px;height:207px;background:var(--tan);border:1px solid #9b5d33;border-radius:3px}
.news .head{height:66px;border-bottom:1px solid #c5613b;position:relative}
.news .env{position:absolute;left:27px;top:22px}
.news .t1{position:absolute;left:66px;top:12px;color:#fff;font-size:12.5px;font-weight:300}
.news .t2{position:absolute;left:66px;top:26px;color:#f6c35a;font-size:20px;font-weight:300}
.news p{color:#fff;font-size:8.5px;font-weight:600;line-height:14px;padding:12px 16px 0 21px}
.news .field{margin:14px 0 0 21px;width:170px;height:28px;background:#fff;border:1px solid #d9c2ad;font-size:8.5px;font-style:italic;color:#999;padding:8px 11px}
.news .submit{position:absolute;right:16px;bottom:20px;width:62px;height:19px;border-radius:9px;background:linear-gradient(#f8c84a,#e89e1f);color:#8a4a1a;font-size:10px;font-weight:600;font-style:italic;text-align:center;line-height:19px}
.slider{left:282px;top:214px;width:539px;height:207px;border:4px solid var(--cream);background:linear-gradient(90deg,#f3f3f1,#e8e8e4)}
.slider .photo{position:absolute;right:2px;top:0;width:222px;height:199px;background:linear-gradient(90deg,rgba(232,232,228,0),#d9d3a8 40%,#b89a2a 70%,#e4e0cf)}
.slider .k1{position:absolute;left:18px;top:62px;font-size:26px;font-weight:300;color:#444}
.slider .k2{position:absolute;left:17px;top:88px;font-size:42px;font-weight:300;color:var(--orange);letter-spacing:.5px}
.dots{position:absolute;left:19px;top:181px;display:flex;gap:9px}
.dots i{width:7px;height:7px;border-radius:50%;background:#999}
.dots i.on{background:var(--orange)}
.psearch{left:70px;top:436px;width:205px;height:62px;background:var(--cream)}
.psearch h4{font-weight:400;font-size:10.5px;color:var(--brown);padding:9px 0 0 13px}
.psearch .box{margin:6px 0 0 13px;width:180px;height:22px;background:#fff;border:1px solid #cfcbb0;font-size:8px;font-style:italic;color:#aaa;padding:5px 8px;display:flex;justify-content:space-between}
.cats{left:70px;top:510px;width:205px;height:290px;background:var(--cream);list-style:none}
.cats li{height:28px;border-bottom:1px solid #d2ceb2;font-size:10px;color:var(--brown);display:flex;align-items:center;padding-left:24px}
.cats li:last-child{border-bottom:none}
.cats li::before{content:"";width:4px;height:4px;border-radius:50%;background:#c47a35;margin-right:14px}
.offers{left:70px;top:806px;width:205px;height:172px;border:4px solid #ecebe3;background:#fff}
.offers h3{font-weight:300;font-size:20px;color:var(--red);padding:4px 0 0 18px;height:36px;border-bottom:1px solid #ddd;margin:0 5px}
.offers p{font-size:8.5px;line-height:13px;padding:8px 12px 0 17px;color:#666}
.offers .img{position:absolute;left:19px;top:80px;width:70px;height:80px;background:linear-gradient(#e7d06a,#b9952a)}
.offers .old{position:absolute;left:118px;top:82px;font-size:17px;color:#666;text-decoration:line-through}
.offers .new{position:absolute;left:112px;top:104px;font-size:19px;font-weight:600;color:var(--red)}
.offers .btn{position:absolute;left:105px;top:131px;width:88px;height:23px;background:#555;border:2px solid #888;color:#eee;font-size:11px;text-align:center;line-height:19px}
.pay{left:81px;top:990px;font-size:9px;color:#555}
.cards{left:81px;top:1015px;display:flex;gap:6px}
.cards i{width:22px;height:14px;border-radius:2px;background:#dfe3ea;border:1px solid #b8bdc8}
.seals{left:81px;top:1048px;display:flex;gap:13px}
.seals i{display:block;height:29px;background:#eee;border:1px solid #aaa}
.foothr{left:70px;top:1094px;width:205px;height:1px;background:#e5e5e5}
.quote{left:282px;top:430px;width:539px;height:68px;background:linear-gradient(90deg,#fff,#f1f1ee);font-style:italic;font-weight:300;font-size:15px;line-height:25px;color:var(--brown-mid);padding:12px 18px}
.quote .vial{position:absolute;right:22px;top:14px;width:14px;height:44px;background:linear-gradient(#e6e6e6,#cfcfcf);border-radius:2px}
.rule{left:282px;width:539px;height:3px;background:var(--cream)}
.welcome{left:284px;top:530px;width:530px}
.welcome h2{font-weight:400;font-size:18px;color:var(--red);margin-bottom:12px}
.welcome p{font-size:9.1px;line-height:17px;text-align:justify;margin-bottom:5px;color:#707070}
.pill{display:inline-block;height:20px;padding:0 11px;border-radius:10px;background:linear-gradient(#a96a3e,#87502b);color:#fff;font-size:9.5px;line-height:20px}
.col{top:896px;width:164px}
.col h3{font-weight:400;font-size:15.5px;color:var(--red);margin-bottom:7px}
.col .ph{width:164px;height:88px;border:2px solid #eee}
.col p{font-size:8.6px;line-height:15.5px;color:#707070;margin:12px 0 13px}
.col .pill{height:19px;line-height:19px;font-size:8.5px;padding:0 10px}
.footer{left:66px;top:1130px;width:758px;height:66px;background:var(--dark);color:#eee;font-size:8.5px}
.footer .links{position:absolute;left:12px;top:14px;display:flex;gap:6px}
.footer .copy{position:absolute;left:12px;top:38px}
.social{position:absolute;right:12px;top:18px;display:flex;gap:9px}
.social i{width:24px;height:24px;border-radius:50%;background:#6d7f95;border:2px solid #9aa8b8}
</style>
</head>
<body>
<div class="band"></div>

<div class="abs toplinks">
  <span><svg width="11" height="11" viewBox="0 0 11 11"><circle cx="5.5" cy="3" r="2.6" fill="#b2282b"/><path d="M0.5 11c0-3 2.2-4.6 5-4.6s5 1.6 5 4.6z" fill="#b2282b"/></svg>My Account</span><span class="sep">|</span>
  <span><svg width="12" height="11" viewBox="0 0 12 11"><path d="M0.5 1h2l1.6 6h6l1.3-4.3H3.2" fill="none" stroke="#b2282b" stroke-width="1.2"/><circle cx="4.8" cy="9.3" r="1" fill="#b2282b"/><circle cx="9.2" cy="9.3" r="1" fill="#b2282b"/></svg>My Cart</span><span class="sep">|</span>
  <span>Log in</span><span class="sep">|</span><span>Register</span>
</div>

<div class="abs sheet"></div>

<div class="abs brand"><span class="mark"></span>Saveurs Du Matin</div>

<div class="abs search"><span>Search</span><svg width="9" height="9" viewBox="0 0 9 9"><circle cx="3.6" cy="3.6" r="2.6" fill="none" stroke="#bbb" stroke-width="1.2"/><path d="M5.6 5.6L8.5 8.5" stroke="#bbb" stroke-width="1.4"/></svg></div>

<nav class="abs nav">
  <a class="active" style="width:80px">Olive oils</a>
  <a style="width:115px">Balsamic Vinegars</a>
  <a style="width:52px">Misc</a>
  <a style="width:108px">Vinegars and oils</a>
  <a style="width:95px">Specialty salts</a>
  <a style="width:97px">Organic spices</a>
  <a style="width:104px">Specialty Spices</a>
  <a style="width:101px">Kitchen Tools</a>
</nav>

<section class="abs news">
  <div class="head">
    <svg class="env" width="28" height="22" viewBox="0 0 28 22"><g transform="rotate(-18 14 11)"><rect x="2" y="3" width="24" height="16" rx="1" fill="#fff"/><path d="M2 3l12 9 12-9" fill="none" stroke="#d8c9bb" stroke-width="1"/></g></svg>
    <div class="t1">Subscribe for</div>
    <div class="t2">News Letter</div>
  </div>
  <p>Sed ut perspiciatis unde omnis iste natus error sit voluptatem accusantium.</p>
  <div class="field">Enter your mail ID</div>
  <div class="submit">SUBMIT</div>
</section>

<section class="abs slider">
  <div class="photo" role="img" aria-label="Corked glass bottle of golden olive oil beside a small glass of oil"></div>
  <div class="k1">The Finnest</div>
  <div class="k2">OLIVE OILS</div>
  <div class="dots"><i class="on"></i><i></i><i></i><i></i></div>
</section>

<div class="abs psearch">
  <h4>Product Search</h4>
  <div class="box"><span>Enter Key word...</span><svg width="8" height="8" viewBox="0 0 9 9"><circle cx="3.6" cy="3.6" r="2.6" fill="none" stroke="#bbb" stroke-width="1.2"/><path d="M5.6 5.6L8.5 8.5" stroke="#bbb" stroke-width="1.4"/></svg></div>
</div>

<ul class="abs cats">
  <li>Extra Virgin Olive Oils</li>
  <li>Flavored Olive Oils</li>
  <li>Specialty Oils</li>
  <li>Aceto Balsamico Tradizionale</li>
  <li>Traditional Style Aged Balsamic</li>
  <li>White Balsamics</li>
  <li>Wine Vinegars</li>
  <li>Specialty Foods</li>
  <li>Accessories</li>
  <li>Cruets &amp; Dipping Dishes</li>
</ul>

<section class="abs offers">
  <h3>Special Offers</h3>
  <p>Nor again is there anyone who loves or because it is pain.</p>
  <div class="img" role="img" aria-label="Assorted bottles of flavoured olive oil with herbs"></div>
  <div class="old">$00.00</div>
  <div class="new">$00.00</div>
  <div class="btn">VIEW MORE</div>
</section>

<div class="abs pay">Payments :</div>
<div class="abs cards"><i></i><i></i><i></i><i></i><i></i></div>
<div class="abs seals"><i style="width:90px"></i><i style="width:73px"></i></div>
<div class="abs foothr"></div>

<div class="abs quote">Sed ut perspiciatis unde omnis iste natus error sit voluptatem accusantium doloremque laudantium, totam rem aperiam.<span class="vial"></span></div>
<div class="abs rule" style="top:510px"></div>

<section class="abs welcome">
  <h2>Welcome to our site</h2>
  <p>Sed ut perspiciatis unde omnis iste natus error sit voluptatem accusantium doloremque laudantium, totam rem aperiam, eaque ipsa quae ab illo inventore veritatis et quasi architecto beatae vitae dicta sunt explicabo. Nemo enim ipsam voluptatem quia voluptas sit aspernatur aut odit aut fugit, sed quia consequuntur magni dolores eos qui ratione voluptatem sequi nesciunt. Neque porro quisquam est, qui dolorem ipsum quia dolor sit amet, consectetur, adipisci velit, sed quia non numquam eius modi tempora incidunt ut labore et dolore magnam aliquam quaerat voluptatem.</p>
  <p>Ut enim ad minima veniam, quis nostrum exercitationem ullam corporis suscipit laboriosam, nisi ut aliquid ex ea commodi consequatur. Quis autem vel eum iure reprehenderit qui in ea voluptate velit esse quam nihil molestiae consequatur, vel illum qui dolorem eum fugiat quo voluptas nulla pariatur. But I must explain to you how all this mistaken idea of denouncing pleasure and praising pain was born and I will give you a complete account of the system, and expound the actual teachings of the great explorer of the truth, the master-builder of human happiness.</p>
  <p>No one rejects, dislikes, or avoids pleasure itself, because it is pleasure, but because those who do not know how to pursue pleasure rationally encounter consequences that are extremely painful. Nor again is there anyone who loves or pursues or desires to obtain pain of itself, because it is pain, but because occasionally circumstances occur in which toil and pain can procure him some great pleasure.</p>
  <span class="pill" style="margin-top:12px">View more</span>
</section>

<div class="abs rule" style="top:875px"></div>

<section class="abs col" style="left:283px">
  <h3>About us</h3>
  <div class="ph" role="img" aria-label="Glass of olive oil with olive branch" style="background:linear-gradient(90deg,#5f5a1e,#c9a529 55%,#f1eee2)"></div>
  <p>Nor again is there anyone who loves or because it is pain, and but not because occasion ally circumstances occur.</p>
  <span class="pill">View more</span>
</section>
<section class="abs col" style="left:469px">
  <h3>Our Products</h3>
  <div class="ph" role="img" aria-label="Olive oil bottle lying among green olives" style="background:linear-gradient(160deg,#f3f0de,#d7b52e 45%,#7d8a2a 80%,#f4f2e6)"></div>
  <p>Nor again is there anyone who loves or because it is pain, and but not because occasion ally circumstances occur.</p>
  <span class="pill">View more</span>
</section>
<section class="abs col" style="left:656px">
  <h3>Kitchen Tools</h3>
  <div class="ph" role="img" aria-label="Spoon of olive oil over fresh salad leaves" style="background:linear-gradient(135deg,#7aa23a,#c5d35a 45%,#e3d46a 65%,#5e8a2c)"></div>
  <p>Nor again is there anyone who loves or because it is pain, and but not because occasion ally circumstances occur.</p>
  <span class="pill">View more</span>
</section>

<footer class="abs footer">
  <div class="links"><span>Home</span>|<span>Olive oils</span>|<span>Balsamic Vinegars</span>|<span>Misc</span>|<span>Vinegars and oils</span>|<span>Specialty salts</span>|<span>Organic spices</span>|<span>pecialty Spices</span>|<span>Kitchen Tools</span></div>
  <div class="copy">Copyright &copy; 2012 www.saveursdumatin.example &nbsp;&nbsp; All rights reserved.</div>
  <div class="social"><i></i><i></i><i></i><i style="background:#8a6a5e;border-color:#b59a8e"></i></div>
</footer>
</body>
</html>
```